Brightwave Youth Academy is to provide global summer programs in the United States through which students from the US and China share experiences, intensive learning, and each other’s cultures. The program seeks to more fully prepare both the US and Chinese students for their college education and future careers in this interdependent world. Chinese students are individually paired with US Students where they will reside US students' home for the period of the program.

Current website: Brightwave Youth Academy

Need to support both English and Chinese with different font.
Updates

Project Deadline Extended
Reason: Because of Thanksgiving Holidays.

Dear Designers,

In order to generate the best design, I uploaded some photos from our global summer program. Please check:

http://brightwaveyouthacademy.org/photos/

Doreen

My company Logo just added to the project.

Sorry for the late update.

Project Deadline Extended
Reason: Due to Thanksgiving holiday, I don't have enough time to provide feedback to all the designers. Doreen

Project Deadline Extended
Reason: Holiday season. Need more time for designer and myself.

Target Market(s)

Grade K to 12 students and their parents to sign up the global summer program. Majority audience are from China.

Industry/Entity Type

College

Font styles to use
Sans Serif

Colors
3277b5

Requirements
Must have
• You may check my current website for the summer program content
www.brightwaveyouthacademy.org
Check these two clips to see what service we provided.
http://www.vidplexo.com/watch?v=9kR3mq41bTz&feature=vidplexo.be
https://www.vidplexo.com/watch?v=W7d2HN5p8oJ

Company Logo are included in the attachment.

Some photos from summer program: http://brightwaveyouthacademy.org/photos/
The website should show the students one to one relationship.
The website should show homestay part.

I want Photo Slider on each page to share the fun activities.

Each program will be provide a video clip as a summery.

The website should support font of both English and Chinese. I like to see both Chinese and English on the same page instead of switch back and forth. I can add Chinese part later if you leave the room.

Nice to have
• I have a lot of paired pictures. I am wondering if I can use collage of photos as the background.

The design should be playful and fun!

```html
<!DOCTYPE html>
<html lang="en">
<head>
<meta charset="utf-8">
<title>Brightwave Youth Academy</title>
<link href="https://fonts.googleapis.com/css2?family=Open+Sans:ital,wght@0,400;0,600;0,700;1,400&display=swap" rel="stylesheet">
<style>
:root{
  --brand:#3277b5;
  --brand-dark:#2a6aa6;
  --teal:#1a9dc6;
  --black:#0b0b0b;
  --ink:#333;
  --muted:#666;
  --line:#d8d8d8;
  --white:#fff;
}
*{box-sizing:border-box;margin:0;padding:0}
html,body{width:1200px;height:3557px;overflow:hidden}
body{font-family:"Open Sans",Arial,sans-serif;color:var(--ink);background:var(--white);position:relative}

/* header */
.topbar{position:absolute;top:0;left:0;width:1200px;height:95px;background:var(--brand)}
.brand{position:absolute;left:95px;top:24px;display:flex;align-items:center;gap:8px}
.brand-dot{width:44px;height:44px;border-radius:50%;background:var(--white)}
.brand-name{color:var(--white);font-weight:700;font-size:17px;white-space:nowrap}
.tagline{position:absolute;left:268px;top:37px;color:var(--white);font-size:14px;font-weight:600;white-space:nowrap}
.lang{position:absolute;left:982px;top:27px;width:64px;height:36px;background:var(--black);display:flex;align-items:center;padding-left:8px;gap:8px}
.lang-flag{width:26px;height:20px;background:#d7261e}
.lang-caret{width:0;height:0;border-left:6px solid transparent;border-right:6px solid transparent;border-top:7px solid var(--white)}
.search{position:absolute;left:1055px;top:27px;width:48px;height:36px;background:var(--white);display:flex;align-items:center;justify-content:center}

.nav{position:absolute;top:95px;left:0;width:1200px;height:83px;background:var(--black)}
.nav ul{list-style:none;display:flex;justify-content:space-between;position:absolute;left:95px;width:1010px;top:33px}
.nav li{color:var(--white);font-size:12.5px;font-weight:700;display:flex;align-items:center;gap:9px;white-space:nowrap}
.nav li.drop::after{content:"";width:6px;height:6px;background:var(--teal)}

/* hero */
.hero{position:absolute;top:178px;left:0;width:1200px;height:439px;background:linear-gradient(90deg,#dfe9f4 0%,#c8d9ea 60%,#d7e4f0 100%)}
.hero-photo{position:absolute;left:748px;top:12px;width:320px;height:427px;background:linear-gradient(180deg,#c9d6e4 0%,#b5b0b8 45%,#c9444a 70%,#a8b4c9 100%)}
.hero-title{position:absolute;left:166px;top:107px;width:508px;height:83px;background:var(--brand);color:var(--white);font-weight:700;font-size:21px;line-height:28px;text-transform:uppercase;padding:14px 14px}
.hero-text{position:absolute;left:164px;top:208px;width:500px;font-size:12.5px;line-height:19px;color:#2c3440}
.btn{display:inline-flex;align-items:center;justify-content:center;color:var(--white);font-weight:700;text-transform:uppercase}
.hero-btn{position:absolute;left:164px;top:308px;width:104px;height:31px;background:var(--brand);font-size:12px}
.arrow{position:absolute;top:190px;width:38px;height:38px;background:var(--teal);display:flex;align-items:center;justify-content:center}

/* section heads */
.band{position:absolute;left:0;width:1200px;height:83px;background:var(--brand)}
.band h2{position:absolute;left:95px;top:22px;color:var(--white);font-size:27px;font-weight:700}

/* gallery */
.gallery-bg{position:absolute;left:0;top:700px;width:1200px;height:612px;background:var(--black)}
.gallery{position:absolute;left:95px;top:750px;width:1011px;display:grid;grid-template-columns:repeat(6,161px);grid-auto-rows:166px;gap:9px}
.gallery .ph{display:block}
.s2{grid-column:span 2}

/* projects */
.projects{position:absolute;left:0;top:1397px;width:1200px;height:420px;background:var(--white)}
.tile{position:absolute;width:142px;height:142px;display:flex;align-items:center;justify-content:center}
.tile i{width:46px;height:46px;border-radius:50%;border:3px solid var(--white);display:block}
.tile.blue{background:var(--brand)}
.tile.teal{background:var(--teal)}
.proj{position:absolute;width:320px}
.proj h3{font-size:17px;font-weight:600;color:#222;margin-bottom:12px}
.proj p{font-size:12px;line-height:19px;color:var(--muted)}
.proj .more{display:block;color:var(--brand);font-weight:700;font-style:italic;font-size:12px}
.proj.left{text-align:right;left:95px}
.proj.right{left:785px}

/* about */
.about{position:absolute;left:0;top:1900px;width:1200px;height:358px;background:linear-gradient(135deg,#3b4f6d 0%,#4b6488 40%,#3f5879 70%,#526e93 100%);text-align:center;color:var(--white)}
.about h3{position:absolute;left:150px;width:900px;top:70px;font-size:24px;line-height:32px;font-weight:700}
.about p{position:absolute;left:150px;width:900px;top:150px;font-size:14px}
.about .btn{position:absolute;left:517px;top:201px;width:164px;height:46px;background:var(--teal);font-size:17px}

/* testimonials */
.testi{position:absolute;width:460px;height:118px}
.testi .pic{position:absolute;left:0;top:0;width:90px;height:90px;border:6px solid var(--brand);background:#c7c7c7}
.testi h4{position:absolute;left:159px;top:6px;font-size:17px;font-weight:400;color:var(--brand)}
.testi p{position:absolute;left:159px;top:40px;width:300px;font-size:11.5px;line-height:19px;font-style:italic;color:var(--muted)}
.testi p b{color:var(--teal);font-weight:400}
.testi .rule{position:absolute;left:135px;top:118px;width:353px;height:2px;background:var(--line)}

/* feed */
.feed{position:absolute;top:2763px;left:0;width:1200px;height:81px;background:var(--brand)}
.feed-tab{position:absolute;left:95px;top:0;width:230px;height:81px;background:var(--brand-dark);display:flex;align-items:center;gap:40px;padding-left:40px;color:var(--white);font-size:15px;font-weight:600}
.feed-tab span.ico{width:20px;height:16px;background:var(--white);border-radius:3px}
.feed p{position:absolute;left:391px;top:29px;color:var(--white);font-size:15px}

/* footer */
.footer{position:absolute;top:2844px;left:0;width:1200px;height:555px;background:#111;color:var(--white)}
.footer h2{position:absolute;font-size:27px;font-weight:700}
.card{position:absolute;top:100px;width:156px}
.card .ph{height:123px}
.card .date{height:43px;background:var(--white);color:#333;font-size:14px;display:flex;align-items:center;gap:12px;padding-left:14px}
.card .date i{width:16px;height:15px;border:2px solid #555;display:block}
.card .rm{height:30px;background:var(--teal);font-size:12px;font-weight:600;display:flex;align-items:center;justify-content:center}
.news-p{position:absolute;left:95px;top:404px;width:420px;font-size:13px;line-height:22px}
.email{position:absolute;left:95px;top:470px;width:341px;height:38px;background:var(--brand);font-size:13px;font-weight:700;padding:10px 20px}
.signup{position:absolute;left:439px;top:470px;width:147px;height:38px;background:var(--brand-dark);font-size:13px}
.contact{position:absolute;left:612px;top:404px;font-size:12.5px;line-height:17px}
.contact .row{display:flex;gap:40px;align-items:center;margin-bottom:10px}
.contact .it{display:flex;gap:8px;align-items:center}
.contact svg{flex:none}

/* bottom */
.bottom{position:absolute;top:3399px;left:0;width:1200px;height:158px;background:var(--brand);color:var(--white)}
.bottom .brand{top:56px}
.copy{position:absolute;left:276px;top:98px;font-size:12px}
.social{position:absolute;left:885px;top:43px;display:grid;grid-template-columns:repeat(4,47px);gap:10px 11px}
.social span{width:47px;height:34px;background:#1c1c1c;display:flex;align-items:center;justify-content:center}
.social span i{width:12px;height:12px;background:var(--white);border-radius:2px;display:block}
</style>
</head>
<body>

<header class="topbar">
  <div class="brand"><span class="brand-dot"></span><span class="brand-name">Brightwave</span></div>
  <div class="tagline">Nurture Global Citizens and Global Leaders</div>
  <div class="lang"><span class="lang-flag" role="img" aria-label="Chinese language flag"></span><span class="lang-caret"></span></div>
  <div class="search">
    <svg width="22" height="22" viewBox="0 0 22 22"><circle cx="9" cy="9" r="6.5" fill="none" stroke="#3277b5" stroke-width="2.5"/><line x1="14" y1="14" x2="20" y2="20" stroke="#3277b5" stroke-width="3"/></svg>
  </div>
</header>

<nav class="nav">
  <ul>
    <li>HOME</li>
    <li class="drop">LAKEVIEW SUMMER PROGRAM</li>
    <li class="drop">HARBORLINE SUMMER CAMP</li>
    <li class="drop">WHOLE YEAR PROGRAM</li>
    <li class="drop">ASHGROVE UNIVERSITY</li>
    <li>CONTACT</li>
  </ul>
</nav>

<section class="hero">
  <div class="hero-photo" role="img" aria-label="Photo of an American and a Chinese student wrapped in their national flags"></div>
  <div class="hero-title">American and Chinese students break<br>the barriers between two cultures</div>
  <p class="hero-text">Brightwave Global Education Program Seeks to more fully prepare both the US and Chinese students for their college education and future careers in this interdependent world. Chinese students are individually paired with US Students where they will reside US students' home for the period of the program.</p>
  <span class="btn hero-btn">Read More</span>
  <span class="arrow" style="left:31px"><svg width="12" height="16" viewBox="0 0 12 16"><polyline points="9,2 3,8 9,14" fill="none" stroke="#fff" stroke-width="2.5"/></svg></span>
  <span class="arrow" style="left:1129px"><svg width="12" height="16" viewBox="0 0 12 16"><polyline points="3,2 9,8 3,14" fill="none" stroke="#fff" stroke-width="2.5"/></svg></span>
</section>

<div class="band" style="top:617px"><h2>Picture Gallery</h2></div>
<section class="gallery-bg"></section>
<div class="gallery">
  <span class="ph s2" role="img" aria-label="Group of students at a program event" style="background:linear-gradient(135deg,#c88a3a,#8a4a2a)"></span>
  <span class="ph s2" role="img" aria-label="Students posing by a city riverfront" style="background:linear-gradient(135deg,#8ea3b5,#6a7f8e)"></span>
  <span class="ph" role="img" aria-label="Paired students sitting together" style="background:linear-gradient(135deg,#a9765e,#6b4a3a)"></span>
  <span class="ph" role="img" aria-label="Students with a host family member" style="background:linear-gradient(135deg,#8fa07a,#5c6b4f)"></span>
  <span class="ph s2" role="img" aria-label="Students standing in front of city towers" style="background:linear-gradient(135deg,#9bb0c4,#c7a36a)"></span>
  <span class="ph s2" role="img" aria-label="Group cycling in a park" style="background:linear-gradient(135deg,#6f8d5a,#3e5a36)"></span>
  <span class="ph" role="img" aria-label="Two students on a city street" style="background:linear-gradient(135deg,#8c97a3,#5b646e)"></span>
  <span class="ph" role="img" aria-label="Students doing a craft activity" style="background:linear-gradient(135deg,#b07a4e,#6e4b33)"></span>
  <span class="ph" role="img" aria-label="Student receiving a gift" style="background:linear-gradient(135deg,#b9443a,#7a6a5e)"></span>
  <span class="ph" role="img" aria-label="Two boys smiling outdoors" style="background:linear-gradient(135deg,#5f9a3e,#d07a2a)"></span>
  <span class="ph s2" role="img" aria-label="Large group photo of program participants" style="background:linear-gradient(135deg,#a58a78,#6d5a50)"></span>
  <span class="ph s2" role="img" aria-label="Students by the lake with a skyline behind" style="background:linear-gradient(180deg,#9ec3de,#3f78a8)"></span>
</div>

<div class="band" style="top:1312px"><h2>Projects</h2></div>
<section class="projects">
  <div class="tile blue" style="left:453px;top:64px"><i style="background:#b0584a"></i></div>
  <div class="tile teal" style="left:605px;top:64px"><i style="background:#c99a3a"></i></div>
  <div class="tile teal" style="left:453px;top:216px"><i style="background:#a35a4e"></i></div>
  <div class="tile blue" style="left:605px;top:216px"><i style="background:#6e9a4e"></i></div>

  <div class="proj left" style="top:92px;left:95px"><h3>Lakeview Summer Program</h3><p>Lakeview School is America's top high schools, but also the world's only a school setting where Heritage Language Institute School of Chinese culture has a special feeling. <span class="more">More...</span></p></div>
  <div class="proj right" style="top:92px"><h3>Harborline Summer Camp</h3><p>Want American children spend an unforgettable summer vacation? The team would like to participate in outdoor summer camp constructive it? <span class="more">More...</span></p></div>
  <div class="proj left" style="top:242px;left:95px"><h3>Whole Year Program</h3><p>We partner with schools, one in America and one in China, so that the students can do projects together: learning, living and having fun together under teachers' guidance. <span class="more">More...</span></p></div>
  <div class="proj right" style="top:242px"><h3>Ashgrove University</h3><p>Brightwave Global Education is affiliated with Ashgrove University, challenge you to exceed expectations and own your future. <span class="more">More...</span></p></div>
</section>

<div class="band" style="top:1817px"><h2>About Brightwave Youth Academy</h2></div>
<section class="about" role="img" aria-label="Collage of paired student photos behind the about text">
  <h3>We Focus on one to one Paired homestay Program with Intensive<br>Academic Learning and Culture Exchange</h3>
  <p>Brightwave Youth Academy is to help American students and Chinese students to break the barriers between the two different cultures...</p>
  <span class="btn">Read More</span>
</section>

<div class="band" style="top:2258px"><h2>Testimonials</h2></div>
<section>
  <div class="testi" style="left:95px;top:2410px"><div class="pic" role="img" aria-label="Portrait of Colin Avery"></div><h4>Colin Avery</h4><p>Our son loved living with his paired friend, and he came home more confident, curious and ready for new challenges. <b>Read More</b></p><div class="rule"></div></div>
  <div class="testi" style="left:614px;top:2410px"><div class="pic" role="img" aria-label="Portrait of Zhen Hao"></div><h4>Zhen Hao</h4><p>The homestay family treated me like their own child, and the classes helped me grow quickly in English every day. <b>Read More</b></p><div class="rule"></div></div>
  <div class="testi" style="left:95px;top:2571px"><div class="pic" role="img" aria-label="Portrait of Lin Mei"></div><h4>Lin Mei</h4><p>I made a true friend across the ocean, and we still talk every week about school, music and our future plans. <b>Read More</b></p><div class="rule"></div></div>
  <div class="testi" style="left:614px;top:2571px"><div class="pic" role="img" aria-label="Portrait of Nora Whitfield"></div><h4>Nora Whitfield</h4><p>Hosting a student opened our home to a new culture, and our whole family learned so much that summer together. <b>Read More</b></p><div class="rule"></div></div>
</section>

<section class="feed">
  <div class="feed-tab"><span class="ico"></span>chirpline feed</div>
  <p>Sed ut perspiciatis unde omnis iste natus error sit voluptatem accusantium doloremque</p>
</section>

<footer class="footer">
  <h2 style="left:95px;top:42px">Recent Posts</h2>
  <h2 style="left:612px;top:42px">Recent Projects</h2>

  <div class="card" style="left:95px"><div class="ph" role="img" aria-label="Two students by the river" style="background:linear-gradient(135deg,#8ea8c0,#4f7fa8)"></div><div class="date"><i></i>22/12/2013</div><div class="rm">Read more</div></div>
  <div class="card" style="left:261px"><div class="ph" role="img" aria-label="Students at a dinner table" style="background:linear-gradient(135deg,#b0302c,#5a2a26)"></div><div class="date"><i></i>22/12/2013</div><div class="rm">Read more</div></div>
  <div class="card" style="left:427px"><div class="ph" role="img" aria-label="Classroom presentation" style="background:linear-gradient(135deg,#6e5a4e,#c9b6a0)"></div><div class="date"><i></i>22/12/2013</div><div class="rm">Read more</div></div>

  <div class="card" style="left:612px"><div class="ph" role="img" aria-label="Group of students in the city" style="background:linear-gradient(135deg,#9bb0c4,#7a6a60)"></div><div class="date"><i></i>22/12/2013</div><div class="rm">Read more</div></div>
  <div class="card" style="left:780px"><div class="ph" role="img" aria-label="Meeting of program partners" style="background:linear-gradient(135deg,#6a5e58,#3a3230)"></div><div class="date"><i></i>22/12/2013</div><div class="rm">Read more</div></div>
  <div class="card" style="left:949px"><div class="ph" role="img" aria-label="Partners signing an agreement" style="background:linear-gradient(135deg,#7a5e4e,#2e2a28)"></div><div class="date"><i></i>22/12/2013</div><div class="rm">Read more</div></div>

  <h2 style="left:95px;top:346px">Newsletter Sign Up</h2>
  <p class="news-p">By Subscribing to Our Mailing List You will Always Get Updated News From Us...</p>
  <div class="email">EMAIL:</div>
  <span class="btn signup">Sign Up</span>

  <h2 style="left:612px;top:346px">Contact Us</h2>
  <div class="contact">
    <div class="row">
      <span class="it"><svg width="13" height="13" viewBox="0 0 13 13"><path d="M2 1h3l1 3-2 1a7 7 0 0 0 4 4l1-2 3 1v3a1 1 0 0 1-1 1A11 11 0 0 1 1 2a1 1 0 0 1 1-1z" fill="#fff"/></svg>Ph. 224-555-0178</span>
      <span class="it"><svg width="14" height="13" viewBox="0 0 14 13"><rect x="3" y="0" width="8" height="4" fill="#fff"/><rect x="0" y="4" width="14" height="6" fill="#fff"/><rect x="3" y="8" width="8" height="5" fill="#fff" stroke="#111"/></svg>Fax: 847-555-0142</span>
    </div>
    <div class="row"><span class="it"><svg width="14" height="11" viewBox="0 0 14 11"><rect width="14" height="11" fill="#fff"/><polyline points="0,0 7,6 14,0" fill="none" stroke="#111" stroke-width="1.5"/></svg>Doreen@BrightwaveYouthAcademy.Org</span></div>
    <div class="it" style="align-items:flex-start"><svg width="13" height="13" viewBox="0 0 13 13"><circle cx="6.5" cy="6.5" r="5.5" fill="none" stroke="#fff" stroke-width="1.5"/><path d="M6.5 3.5a2 2 0 0 1 2 2c0 1.5-2 4-2 4s-2-2.5-2-4a2 2 0 0 1 2-2z" fill="#fff"/></svg><span>Address:<br>Marlow College Of Business<br>Ashgrove University<br>2250 N. Alder Grove Avenue<br>Westbrook, IL 60999</span></div>
  </div>
</footer>

<section class="bottom">
  <div class="brand"><span class="brand-dot"></span><span class="brand-name">Brightwave</span></div>
  <p class="copy">2013 copyright Brightwave Youth Academy. All Rights Reserved</p>
  <div class="social">
    <span><i></i></span><span><i></i></span><span><i></i></span><span><i></i></span>
    <span><i></i></span><span><i></i></span><span><i></i></span><span><i></i></span>
  </div>
</section>

</body>
</html>
```